"KITE" Web Design Project

We need a create a webpage for a Streaming device product with sucription that we're going lo launch(like a vexa or plumo box but comes with a possibily of monthly sucription of live tv channels).
The name of the product is "KITE" (kinetic internet television entity)

We are looking for something simple and with quality. Something webpages that we like are www.quillstream.com www.tavimo.tv (our product will be very similar to tavimo so you canuse for the menu an information reference, we're going to be more features because we are based on nimbix so users can download all the apps from the lumen appmart)
Also our remote control are gyroscopic (means like the zarp wand) for many games.
We are working also in the logo so you can also see in our package and logo contest named: "MEDIA STREAMING DEVICE: Package-device-logo" the Design #: 1768146 are the logo that maybe we're going to choose.

this is the link of our manufacturer to have on idea of the features of the device;
http://www.dorvalink.com/pa/hqx417.asp

We like one color on the logo. But we want to see the logo in this colors: white,black ,light blue.

Thanks

Reason: to get better jobs

Hi,
you can use for reference the TAVIMO.TV webpage (look and feel, conten, information and & of pages..) also quillstream.tv as (look & feel).

Information to add:
In the case of the content the basic different is our device is nimbix based. So only for reference of information to add (because we don't like lood and feel!!)  please use the info of  this links:

Spanish:
http://www.trevani.es/
products:
http://www.trevani.es/trevani-KQ418.html
http://www.trevani.es/descargas.html
http://www.trevani.es/about.html
http://www.trevani.es/contact.html
http://www.trevani.es/distribuidores.html

English:
http://www.trevani.com/product.asp?id=166
http://www.trevani.com/news.asp
http://www.trevani.com/support.asp
http://www.trevani.com/where-to-buy.asp
http://www.trevani.com/down.asp?id=1
http://www.trevani.com/about-us.asp

Note: are the same info but we're going to have only one model called: "KITE" . So we're going to by the devices to this manufacturer but we're going to rebranded...

AGAIN WE DON'T LIKE THE LOOK & FEEL OF THE LAST LINKS (ARE HORRIBLE) PLEASE USE AS A REFRENCE OF "LOOK & FEEL"  WWW.TAVIMO.TV OR QUILLSTREAM.COM

https://www.filquarry.com/sh/pq8830kkrt2vumb/W19XbLqnze

This files can help for the branding and pictures

Can you change the photos of the Slatr's per someone looking TV? One of the advantage of our product vrs conventional tv cable service is that we are Unplugged , we are Cord cutters. With our KITE device people can see TV on their home, their office, their vacation home. Because they can tke with them our device and conect to the internet and can see TV. 
Another advantage if for exmple our partnership with http://www.castorio.tv/ so people can use their smartphones and tables as a remote control. But not normal remote control, totally interactive remote control and can share also all the network, my phone, and internet content to the TV by our KITE device. 

Please see the attached file. you can use something similar...

Target Market(s)

under 40 years. young people.

Industry/Entity Type

Tv

```html
<!DOCTYPE html>
<html lang="en">
<head>
<meta charset="utf-8">
<title>KITE – Kinetic Internet Television Entity</title>
<link href="https://fonts.googleapis.com/css2?family=Open+Sans:wght@400;600;700&display=swap" rel="stylesheet">
<style>
:root{
  --blue:#1b82cf;
  --blue-dark:#0f5fa6;
  --title:#2a8bd0;
  --text:#6b7480;
  --heading:#3a4450;
  --rule:#e2e6ea;
  --page:#ffffff;
  --soft:#f2f5f8;
  --green:#8cc63f;
  --green-dark:#6fa52b;
  --bar:#0b3f70;
}
*{box-sizing:border-box;margin:0;padding:0}
html,body{width:1200px;height:2916px;overflow:hidden}
body{font-family:"Open Sans",Arial,sans-serif;color:var(--text);background:var(--page);font-size:15px;line-height:1.6}
.wrap{width:840px;margin:0 auto;position:relative}
.btn{display:inline-block;background:var(--green);color:#fff;font-size:13px;font-weight:600;padding:7px 16px;border-radius:3px;border-bottom:2px solid var(--green-dark)}

/* header */
.site-header{height:130px;background:#fff;border-bottom:1px solid var(--rule)}
.site-header .wrap{height:130px;display:flex;align-items:center;justify-content:space-between}
.brand{display:flex;align-items:center;gap:12px;font-size:40px;font-weight:700;color:var(--blue);letter-spacing:1px}
.brand-dot{width:44px;height:44px;border-radius:50%;background:var(--blue)}
.main-nav{display:flex;gap:30px;font-size:15px;color:var(--heading)}
.main-nav .active{color:var(--blue);font-weight:600}

/* hero */
.hero{height:290px;background:linear-gradient(180deg,#2592df 0%,var(--blue-dark) 100%);position:relative;color:#fff}
.hero .wrap{height:290px;display:flex;align-items:center;justify-content:space-between}
.hero-copy{width:440px}
.hero-copy h1{font-size:28px;font-weight:600;margin-bottom:12px}
.hero-copy p{font-size:14px;opacity:.9;margin-bottom:18px;line-height:1.6}
.hero-video{width:330px;height:210px;background:linear-gradient(135deg,#3a3f46,#15181c);border:4px solid #fff;box-shadow:0 4px 14px rgba(0,0,0,.3)}
.hero-arrow{position:absolute;top:125px;width:36px;height:40px;background:rgba(0,0,0,.25)}
.hero-arrow.prev{left:0}.hero-arrow.next{right:0}
.slider-dots{height:40px;display:flex;justify-content:center;align-items:center;gap:8px}
.slider-dots span{width:8px;height:8px;border-radius:50%;background:#cfd6dc}
.slider-dots span.on{background:var(--blue)}

/* sections */
.section-title{text-align:center;color:var(--title);font-size:26px;font-weight:600}
.welcome{height:620px;padding-top:40px}
.tv-visual{width:760px;height:480px;margin:36px auto 0;background:linear-gradient(180deg,#2a2d33 0%,#101215 85%,#d5d9de 86%,#f5f6f7 100%);border-radius:4px}
.divider{height:1px;background:var(--rule);width:840px;margin:0 auto}

.feature{height:230px;padding-top:30px}
.feature .wrap{display:flex;justify-content:space-between;align-items:flex-start}
.feature h2{color:var(--title);font-size:18px;font-weight:600;margin-bottom:8px}
.feature p{font-size:13px;line-height:1.7;margin-bottom:14px}
.feature-text{width:400px}
.device-visual{width:260px;height:150px;margin-left:30px;background:linear-gradient(180deg,#3b3f45,#0f1113);border-radius:10px}
.caption{font-size:11px;text-align:center;margin-top:6px;color:#9aa2ab}
.remote-visual{width:220px;height:140px;margin-right:20px;background:linear-gradient(160deg,#4a4e55,#121417);border-radius:70px 20px 70px 20px}

.apps{height:730px;padding-top:26px}
.apps .lead{text-align:center;font-size:14px;margin-top:10px;line-height:1.6}
.store-visual{width:760px;height:540px;margin:26px auto 0;border:1px solid var(--rule);background:linear-gradient(180deg,#f1f1f1 0%,#f1f1f1 8%,#ffffff 8%,#ffffff 14%,#8cc63f 14%,#6ea832 40%,#ffffff 40%,#eef0f2 100%)}

.news{height:200px;padding-top:24px}
.news .wrap{display:flex;justify-content:space-between}
.news-col{width:400px}
.news-col h3{font-size:11px;font-weight:700;color:var(--heading);letter-spacing:.5px;text-transform:uppercase;margin-bottom:10px}
.news-item{font-size:12px;line-height:1.5;margin-bottom:8px}
.news-item a{color:var(--blue)}
.tweet{display:flex;gap:8px;font-size:12px;line-height:1.5;margin-bottom:8px}
.tweet i{flex:none;width:10px;height:10px;margin-top:4px;background:var(--blue);border-radius:2px}

.cta{height:150px;background:var(--soft);border-top:1px solid var(--rule);border-bottom:1px solid var(--rule)}
.cta .wrap{height:150px;display:flex;align-items:center;justify-content:space-between}
.cta h2{color:var(--title);font-size:22px;font-weight:600;margin-bottom:6px}
.cta p{font-size:13px;width:620px;line-height:1.6}

.site-footer{height:210px;margin-top:30px;background:linear-gradient(180deg,var(--blue) 0%,var(--blue-dark) 100%);color:#e4f0fb}
.site-footer .wrap{display:flex;justify-content:space-between;padding-top:30px}
.footer-brand{width:310px}
.footer-brand .brand{color:#fff;font-size:32px;margin-bottom:10px}
.footer-brand .brand-dot{background:#fff;width:34px;height:34px}
.footer-brand p{font-size:11px;line-height:1.6}
.footer-contact{width:220px;font-size:12px;line-height:1.7}
.footer-contact strong{display:block;color:#fff;font-size:13px;line-height:1.4;margin-bottom:6px}
.footer-social{width:240px}
.footer-social strong{display:block;color:#fff;font-size:13px;margin-bottom:8px}
.social-list{display:grid;grid-template-columns:1fr 1fr;gap:6px 14px;font-size:12px}
.social-list span{display:flex;align-items:center;gap:6px}
.social-list span::before{content:"";width:10px;height:10px;background:#fff;opacity:.8;border-radius:2px}

.bottom-bar{height:54px;background:var(--bar);color:#9fbcd8;font-size:11px}
.bottom-bar .wrap{height:54px;display:flex;align-items:center;justify-content:space-between}
.bottom-bar nav{display:flex;gap:16px}
</style>
</head>
<body>

<header class="site-header">
  <div class="wrap">
    <div class="brand"><span class="brand-dot"></span>KITE</div>
    <nav class="main-nav">
      <span class="active">Home</span><span>Live TV</span><span>Apps</span><span>Coverage</span><span>Help</span><span>Login</span>
    </nav>
  </div>
</header>

<section class="hero">
  <svg class="hero-arrow prev" viewBox="0 0 36 40"><path d="M21 12l-8 8 8 8" fill="none" stroke="#fff" stroke-width="3"/></svg>
  <div class="wrap">
    <div class="hero-copy">
      <h1>The Future of Television</h1>
      <p>Watch live channels, movies and apps on any screen in your home, office or vacation place. Cut the cord and take your TV wherever the internet goes with one small device.</p>
      <span class="btn">Learn More</span>
    </div>
    <div class="hero-video" role="img" aria-label="Video player showing a product introduction clip"></div>
  </div>
  <svg class="hero-arrow next" viewBox="0 0 36 40"><path d="M15 12l8 8-8 8" fill="none" stroke="#fff" stroke-width="3"/></svg>
</section>
<div class="slider-dots"><span class="on"></span><span></span><span></span></div>

<section class="welcome">
  <h2 class="section-title">Welcome To KITE – Kinetic Internet Television Entity</h2>
  <div class="tv-visual" role="img" aria-label="Flat screen television showing the Quelvo OS app market home screen"></div>
</section>

<div class="divider"></div>

<section class="feature">
  <div class="wrap">
    <div>
      <div class="device-visual" role="img" aria-label="The KITE streaming box"></div>
      <div class="caption">The KITE Network Entertainment Unit</div>
    </div>
    <div class="feature-text">
      <h2>Latest In Streaming Technology</h2>
      <p>The KITE set top box is based on Quelvo OS 4.2 using a dual core processor. By connecting your TV with HDMI and to the internet, you can turn any normal TV into a smart TV immediately. Browse the web, stream your favourite shows, play games and chat with friends from the sofa.</p>
      <span class="btn">View All Features</span>
    </div>
  </div>
</section>

<section class="feature">
  <div class="wrap">
    <div class="feature-text" style="margin-left:30px">
      <h2>Revolutionary Gyroscopic Remote</h2>
      <p>Point, tilt and swing to control everything on screen. The motion remote turns your living room into a game room and makes menus quick to move through for every member of the family.</p>
      <span class="btn">See It In Action</span>
    </div>
    <div>
      <div class="remote-visual" role="img" aria-label="Gyroscopic motion remote control"></div>
      <div class="caption">Gyroscopic Remote</div>
    </div>
  </div>
</section>

<section class="apps">
  <h2 class="section-title">MILLIONS Of Apps</h2>
  <p class="lead">KITE is Quelvo OS based,<br>which means it is easy to download and install apps straight from the Lumen Appmart.</p>
  <div class="store-visual" role="img" aria-label="Lumen Appmart store page with featured apps and games"></div>
</section>

<div class="divider"></div>

<section class="news">
  <div class="wrap">
    <div class="news-col">
      <h3>Latest from the blog</h3>
      <p class="news-item"><a>Hello world!</a> Welcome to Pressmill. This is your first post, edit or delete it and start blogging.</p>
      <p class="news-item"><a>A new way to stream live channels</a> Our latest update brings faster menus and more live content.</p>
      <span class="btn">Visit the Blog</span>
    </div>
    <div class="news-col">
      <h3>Latest tweets from KITE</h3>
      <p class="tweet"><i></i>How to use your phone as a remote with KITE, step by step guide now online.</p>
      <p class="tweet"><i></i>Cord cutters unite! New live channel packages arriving this month.</p>
    </div>
  </div>
</section>

<section class="cta">
  <div class="wrap">
    <div>
      <h2>The Future of Television is Here</h2>
      <p>Get a subscription for live channels and enjoy every show on your terms. No cables, no contracts, just plug in KITE, connect to the internet and start watching today.</p>
    </div>
    <span class="btn">Buy KITE</span>
  </div>
</section>

<footer class="site-footer">
  <div class="wrap">
    <div class="footer-brand">
      <div class="brand"><span class="brand-dot"></span>KITE</div>
      <p>KITE brings live TV, apps and games to any screen. Take it with you to the office or holiday home and keep watching wherever there is an internet connection.</p>
    </div>
    <div class="footer-contact">
      <strong>Kinetic Internet<br>Television Entity</strong>
      24 Signal Road, Suite 8<br>
      Phone: (555) 010-2480<br>
      Fax: (555) 010-2481<br>
      Email: hello@kitetv.example
    </div>
    <div class="footer-social">
      <strong>Connect with us</strong>
      <div class="social-list">
        <span>RSS</span><span>Friendwall</span>
        <span>Chirply</span><span>Snapstack</span>
        <span>Email</span><span>Linkerly</span>
        <span>Circlr</span><span>Pictogrid</span>
      </div>
    </div>
  </div>
</footer>

<div class="bottom-bar">
  <div class="wrap">
    <span>Copyright © 2013 Kinetic Internet Television Entity. All rights reserved.</span>
    <nav><span>Home</span><span>Live TV</span><span>Apps</span><span>Coverage</span><span>Help</span><span>Login</span></nav>
  </div>
</div>

</body>
</html>
```